Business Card Design Project

Want a modern business card.
Concern is that our email address is long and thus poses a design challenge.
Items like the company name can be omitted from text as it will be available via the logo.

Example:
Gerald Tunstall
President / CEO
Cell 555.304.1182
Office 555.617.2093
geraldt@korvantsolutionsgroup.example
www.korvantsolutionsgroup.example

Target Market(s)

Technical and executive level members of Information Technology companies in the Healthcare industry.

Industry/Entity Type

Business

Colors

Designer to choose colors to be used in the design.

Requirements
Nice to have
• Raised logo, but I am open.

```html
<!DOCTYPE html>
<html lang="en">
<head>
<meta charset="utf-8">
<title>Korvant Solutions Group — Business Card</title>
<link rel="stylesheet" href="https://fonts.googleapis.com/css2?family=Source+Sans+3:wght@400;600&display=swap">
<style>
  :root {
    --stage: #e4e4e8;
    --card-light: #f4f4f8;
    --navy: #203f7f;
    --accent-red: #e02424;
    --white: #ffffff;
  }
  html, body {
    margin: 0;
    padding: 0;
    width: 1200px;
    height: 720px;
    overflow: hidden;
    background: var(--stage);
    font-family: "Source Sans 3", "Myriad Pro", Arial, sans-serif;
  }
  .stage {
    position: relative;
    width: 1200px;
    height: 720px;
  }
  .card {
    position: absolute;
    top: 217px;
    width: 500px;
    height: 286px;
    box-sizing: border-box;
    box-shadow: 0 2px 10px rgba(0, 0, 0, 0.18);
  }
  .card--front {
    left: 60px;
    background: var(--card-light);
  }
  .card--back {
    left: 640px;
    background: var(--navy);
    display: flex;
    align-items: center;
    justify-content: center;
  }
  .brand-name {
    font-weight: 600;
    letter-spacing: 0.04em;
    text-transform: uppercase;
    line-height: 1.05;
    margin: 0;
  }
  .card--front .brand-name {
    position: absolute;
    left: 34px;
    top: 112px;
    font-size: 21px;
    color: var(--navy);
  }
  .card--back .brand-name {
    font-size: 30px;
    color: var(--white);
    text-align: center;
  }
  .contact {
    position: absolute;
    right: 30px;
    top: 88px;
    text-align: right;
    color: var(--navy);
  }
  .contact__name {
    font-size: 15px;
    margin: 0;
    line-height: 1.15;
  }
  .contact__title {
    font-size: 11.5px;
    color: var(--accent-red);
    margin: 0 0 6px;
  }
  .contact__line {
    display: flex;
    justify-content: flex-end;
    align-items: center;
    gap: 5px;
    font-size: 11.5px;
    line-height: 1.45;
    margin: 0;
  }
  .contact__line--web {
    margin-top: 10px;
  }
  .contact__icon {
    width: 10px;
    height: 10px;
    fill: var(--accent-red);
    flex: none;
  }
  .contact__icon--outline {
    fill: none;
    stroke: var(--accent-red);
    stroke-width: 1.2;
  }
</style>
</head>
<body>
<main class="stage">

  <section class="card card--front" aria-label="Card front">
    <p class="brand-name">Korvant<br>Solutions Group</p>

    <div class="contact">
      <p class="contact__name">Gerald Tunstall</p>
      <p class="contact__title">President / CEO</p>

      <p class="contact__line">555.304.1182
        <svg class="contact__icon" viewBox="0 0 10 10" aria-hidden="true"><path d="M2 0.5 L3.6 2.6 L2.8 3.6 C3.5 5 4.8 6.4 6.3 7.1 L7.3 6.3 L9.5 7.9 L8.4 9.5 C4.5 9 1 5.5 0.5 1.6 Z"/></svg>
      </p>
      <p class="contact__line">555.617.2093
        <svg class="contact__icon" viewBox="0 0 10 10" aria-hidden="true"><path d="M0.5 3.5 C2 1.5 8 1.5 9.5 3.5 L8.5 4.8 L6.8 4.2 L6.8 3.4 C5.6 3 4.4 3 3.2 3.4 L3.2 4.2 L1.5 4.8 Z M2.5 5.5 H7.5 L8.5 9.2 H1.5 Z"/></svg>
      </p>

      <p class="contact__line contact__line--web">geraldt@korvantsolutionsgroup.example
        <svg class="contact__icon contact__icon--outline" viewBox="0 0 10 10" aria-hidden="true"><rect x="0.8" y="2" width="8.4" height="6"/><path d="M0.8 2 L5 5.4 L9.2 2"/></svg>
      </p>
      <p class="contact__line">www.korvantsolutionsgroup.example
        <svg class="contact__icon contact__icon--outline" viewBox="0 0 10 10" aria-hidden="true"><circle cx="5" cy="5" r="4.2"/><path d="M0.8 5 H9.2 M5 0.8 C3 3 3 7 5 9.2 M5 0.8 C7 3 7 7 5 9.2"/></svg>
      </p>
    </div>
  </section>

  <section class="card card--back" aria-label="Card back">
    <p class="brand-name">Korvant<br>Solutions Group</p>
  </section>

</main>
</body>
</html>
```